Modern Website Design for an Online Travel Agency.. Design Only!!

Hi there!

We are building an website for our travel agency that caters to tourists traveling to the Cayman Islands. We provide travel information and take bookings for various tours available here.

We need designs for 8 different web page layouts. You can see the layout specifications in two attached documents. We do not have a need for the coding to be done. This will simply act as a blueprint for our developer to build from.

The important pages are the 'Home Page' 'checkout page' and the ‘Checkout Page’ (Page 1 & 10 in the PDF ‘Website Layout’)

The MOST important page is ‘Tour Search Page’ (page 6)

If you intend on only submitting one page design, please submit a design for page 6. Be aware though, the more of these 3 page designs you submit, the more likely we are to move forward with you!

At this stage, we are simply looking to develop the most aesthetic website design layout possible.

- The website should be colour coordinated with the logo. You can most certainly use other colours if you feel they complement the overall design of the website well.

- Everything must be laid out in an EXTREMELY simple & ‘easy to navigate’ way. The key is simplicity & Functionality. There is no need for messy or elaborate graphics.

- The website MUST have a VERY clean and modern appearance.

- We want the main background to be white, but you can use light grey in places to compliment or add dimension if you feel necessary.

- We will appreciate a good use of shadows and especially a good use of icons. (You can see examples of icons we have already designed, we are definitely open to new icon design concepts too)

- We will reward imagination and original thinking! Essentially we want a website with a creative touch and unique design elements, whilst maintaining that clean and simple layout.

- Most importantly!! - Paying attention to the small details will be highly rewarded (A well balanced and seamless use of fonts, colours, dimensions, shadowing, positioning, etc)

If you have any questions, please don’t hesitate to ask.

We’re excited to see your design submissions!

Thank you!!

You can find all the support documents and content at: https://www.filevorra.net/sh/9qm2rtwplexan7c/QQBmTtZnPdLsWEGxvvaJpLmRw?dl=0

Target Market(s)

Tourists

Industry/Entity Type

Travel

Number of Pages Required

5+ page

Font styles to use
Sans Serif

Colors

Designer to choose colors to be used in the design.

Requirements
Must have
• Must be very clean and modern.
• Must be simple and bold
• Must be color coordinated in a way that makes sense
• White background
Nice to have
• Good use of shadows and Icons
Should not have
• Over use of messy graphics
• And design layout which is not right angled (using anything but vertical or horizontal for the edges in the design)

```html
<!DOCTYPE html>
<html lang="en">
<head>
<meta charset="utf-8">
<title>Tide Trip – Your Island Trip Planner</title>
<link rel="stylesheet" href="https://fonts.googleapis.com/css2?family=Poppins:wght@400;500;600&family=Montserrat:wght@400;500;600;700&family=Great+Vibes&family=Oswald:wght@500&display=swap">
<style>
:root{
  --blue:#1a6fd4;
  --blue-deep:#0f63d2;
  --green:#8cc63f;
  --ink:#1d1d1d;
  --muted:#3d3d3d;
  --mist:#e9f1fb;
  --white:#ffffff;
}
*{margin:0;padding:0;box-sizing:border-box}
html,body{width:1200px;height:4225px;overflow:hidden;background:var(--white)}
body{position:relative;font-family:'Montserrat',sans-serif;color:var(--ink)}
.abs{position:absolute}
.backdrop{position:absolute;left:0;top:0;width:1200px;height:4225px}
.header{z-index:5}

/* header */
.brand{left:232px;top:24px;display:flex;align-items:center;gap:8px;font-family:'Poppins',sans-serif;font-weight:600;font-size:26px;color:var(--blue);white-space:nowrap}
.brand .mark{width:26px;height:26px;background:var(--green);border-radius:4px}
.topbar{left:636px;top:10px;display:flex;align-items:center;font-size:9px;font-weight:600;color:var(--muted);white-space:nowrap}
.topbar .dot{width:16px;height:16px;border:1px solid #777;border-radius:50%;margin-right:4px}
.topbar .cur{margin-left:24px}
.topbar .login{margin-left:22px}
.topbar .dest{margin-left:16px;border:1px solid #777;border-radius:14px;padding:6px 16px}
.nav{left:484px;top:46px;width:480px;height:20px;font-size:9.5px;font-weight:700;letter-spacing:.2px}
.nav a{color:var(--ink);text-decoration:none;position:absolute;white-space:nowrap}
.nav a.on{color:var(--blue)}
.nav a.on::after{content:"";position:absolute;left:0;right:0;top:16px;height:2px;background:var(--blue)}

/* hero */
.hero-script{left:136px;top:278px;font-family:'Great Vibes',cursive;font-size:80px;line-height:90px;color:#111;white-space:nowrap}
.hero-title{left:86px;top:382px;font-family:'Poppins',sans-serif;font-weight:600;font-size:62px;letter-spacing:1px;white-space:nowrap}
.hero-title .a{color:var(--blue)}.hero-title .b{color:var(--green)}
.dots{left:766px;top:553px;display:flex;gap:14px}
.dots i{width:8px;height:8px;border:1px solid #fff;display:block}
.dots i.on{background:#fff}

/* shared */
.center{left:0;width:1200px;text-align:center}
.kicker{font-size:11px;font-weight:700;letter-spacing:1.5px}
.h-sec{font-family:'Poppins',sans-serif;font-weight:500;font-size:23px;color:var(--ink)}
.rule{width:44px;height:2px;background:var(--ink);left:578px}
.copy{font-size:9px;line-height:17.5px;color:var(--muted)}
.btn{display:block;height:22px;border-radius:12px;font-size:8px;font-weight:700;color:#fff;text-align:center;line-height:22px;letter-spacing:.4px;box-shadow:0 3px 8px rgba(26,111,212,.25);white-space:nowrap}
.btn.blue{background:var(--blue);width:112px;left:543px}
.btn.green{background:var(--green);box-shadow:0 3px 8px rgba(140,198,63,.3)}
.step-num{width:86px;height:86px;border-radius:50%;background:var(--mist);font-family:'Poppins',sans-serif;font-size:30px;font-weight:500;color:var(--blue);text-align:center;line-height:86px}
.step-title{font-family:'Poppins',sans-serif;font-weight:500;font-size:31px;line-height:37px;color:var(--blue)}
.step-copy{font-size:9.5px;line-height:16.5px;color:var(--muted)}
.right{text-align:right}
.art{border-radius:40px}

/* destinations */
.dest-card{top:3253px;width:233px;height:247px;border-radius:3px;box-shadow:0 6px 14px rgba(0,0,0,.2);background:linear-gradient(180deg,#6fa9c9 0%,#3d8ea8 35%,#6eaa45 70%,#8cc63f 100%);text-align:center;color:#fff}
.dest-card .name{margin-top:112px;font-family:'Oswald',sans-serif;font-size:30px;line-height:36px;white-space:nowrap}
.dest-card .count{font-size:9px;font-weight:600;margin-top:4px}
.dest-card .go{display:inline-block;margin-top:38px;border:1px solid #fff;font-size:8px;font-weight:700;padding:6px 14px}
.fav-card{top:3647px;width:233px;height:246px;background:#fff;box-shadow:0 6px 16px rgba(0,0,0,.16);text-align:center}
.fav-card .ph{height:183px}
.fav-card .lbl{font-size:11px;font-weight:700;letter-spacing:.5px;line-height:63px}
.arrow{top:3756px;width:22px;height:16px}

/* footer */
.footer{left:0;top:4007px;width:1200px;height:218px;background:var(--blue-deep)}
.island{left:945px;top:3870px;width:240px;height:320px;border-radius:45% 45% 50% 50%;background:linear-gradient(180deg,#eaf3f8 0%,#a9d3e6 40%,#7bc04a 55%,#1d5fb8 75%,#0f4fa8 100%)}
.f-brand{left:232px;top:4093px;display:flex;align-items:center;gap:8px;font-family:'Poppins',sans-serif;font-weight:600;font-size:20px;color:#fff}
.f-brand .mark{width:20px;height:20px;background:var(--green);border-radius:3px}
.f-sep{width:1px;height:88px;background:rgba(255,255,255,.4);top:4057px}
.f-col{top:4060px;color:#fff;font-size:9.5px;line-height:15.5px;white-space:nowrap;z-index:2}
.f-col h4{font-size:10px;font-weight:700;letter-spacing:.5px;margin-bottom:6px}
.f-copy{left:425px;top:4164px;color:#fff;font-size:8.5px;letter-spacing:.3px}
.f-social{left:820px;top:4155px;display:flex;gap:8px;z-index:2}
.f-social i{display:block;width:32px;height:32px;border-radius:50%;background:#0a3f8c}
</style>
</head>
<body>

<svg class="backdrop" viewBox="0 0 1200 4225" aria-hidden="true">
  <path fill="#e9f1fb" d="M0,420 C90,410 170,470 200,560 C230,660 300,700 420,720 C520,740 560,800 545,880 C535,935 515,952 470,952 H0 Z"/>
  <path fill="#e9f1fb" d="M0,1410 C200,1450 360,1420 560,1500 C760,1580 900,1600 1000,1700 C1080,1790 1095,2000 1085,2150 C1075,2260 1000,2262 900,2258 L0,2258 Z"/>
  <path fill="#e9f1fb" d="M0,2600 C300,2620 600,2560 900,2540 C1050,2530 1130,2600 1110,2750 C1090,2900 1120,3050 1000,3140 C900,3170 600,3150 0,3160 Z"/>
</svg>

<!-- hero image area -->
<svg class="abs" style="left:0;top:0" width="1200" height="640" role="img" aria-label="Snorkellers swimming in clear turquoise Caribbean water">
  <defs><linearGradient id="sea" x1="0" y1="0" x2="0" y2="1"><stop offset="0" stop-color="#3fc2cf"/><stop offset=".55" stop-color="#1f9fb3"/><stop offset="1" stop-color="#1b6f78"/></linearGradient></defs>
  <path fill="url(#sea)" d="M1040,0 H1200 V200 C1180,250 1170,300 1175,350 C1185,430 1150,480 1090,490 C1040,500 1010,545 960,585 C900,630 800,640 740,605 C690,575 640,600 590,590 C530,575 520,520 540,470 C560,420 500,380 495,320 C490,250 520,200 570,175 C620,150 640,95 720,88 C800,82 900,98 965,84 C1012,72 1022,30 1040,0 Z"/>
</svg>

<!-- header -->
<div class="abs header brand"><span class="mark"></span>TideTrip</div>
<div class="abs header topbar">
  <span class="dot"></span><span class="dot"></span><span class="dot"></span><span class="dot"></span>
  <span class="cur">USD $ ▾</span>
  <span class="login">→ LOGIN</span>
  <span class="dest">DESTINATIONS ⌄</span>
</div>
<nav class="abs header nav">
  <a class="on" style="left:0">HOME</a>
  <a style="left:57px">DISCOVER CAYMAN</a>
  <a style="left:176px">THING TO DO</a>
  <a style="left:265px">MY TRIP PLANNER</a>
  <a style="left:372px">MAP</a>
  <a style="left:421px">CONTACT US</a>
</nav>

<div class="abs hero-script">Welcome to</div>
<div class="abs hero-title"><span class="a">Tide</span> <span class="b">Trip</span></div>
<div class="abs dots"><i class="on"></i><i></i><i></i><i></i></div>

<!-- welcome -->
<div class="abs center kicker" style="top:689px">WELCOME TO</div>
<div class="abs center" style="top:706px;font-family:'Poppins',sans-serif;font-size:33px;font-weight:500;letter-spacing:1px">Tide Trip</div>
<p class="abs copy" style="left:303px;top:782px;width:594px;text-align:center">We are proud travel concierges of the Cayman Islands! We help thousands of tourists visiting Cayman every year arrange vacation getaway catered to their exact needs. With a wealth of local knowledge, we help you avoid unreliable tour operators and find those local hidden gems. Here you can research everything you need to be fully prepared for your travels and also view the complete range of activities available. Once you're ready to move forward, we'll help you fine tune your itinerary and continue to make all the booking arrangements on your behalf.</p>
<a class="abs btn blue" style="top:887px">READ MORE</a>

<!-- step 1 -->
<div class="abs step-num" style="left:278px;top:999px">1.</div>
<div class="abs step-title" style="left:277px;top:1104px">Explore Where<br>You're Going</div>
<p class="abs step-copy" style="left:277px;top:1188px;width:255px">Use our fully comprehensive guide to learn everything you need to know about travel &amp; safety in the country you're interested in traveling to.</p>
<a class="abs btn green" style="left:277px;top:1261px;width:111px">DISCOVER NOW!</a>
<div class="abs art" style="left:598px;top:1016px;width:349px;height:295px;background:linear-gradient(135deg,#d9f0f4,#b9dcf1 55%,#d4ecb3)" role="img" aria-label="Illustration of a traveller planning a trip beside a map screen and a suitcase"></div>

<!-- why -->
<div class="abs center h-sec" style="top:1401px">Why should organizinga vacation be so complicated?</div>
<div class="abs rule" style="top:1445px"></div>
<p class="abs copy" style="left:290px;top:1472px;width:620px;text-align:center">We all know it! Dreaming up a vacation can be tremendous fun. What better than exploring the endless possibilities of your next adventure? But then comes the nitty gritty task of actually pulling a vacation together.</p>
<p class="abs copy" style="left:290px;top:1525px;width:620px;text-align:center">How do you decide on the most suitable activities to experience and the best tour operators to guide you? Despite your best efforts to avoid booking mix-ups, well hidden costs or dishonest tour operators, mishaps can occur and sometimes can be detrimental to your experience abroad.</p>
<a class="abs btn blue" style="top:1589px">READ MORE</a>

<!-- step 2 -->
<div class="abs art" style="left:311px;top:1680px;width:263px;height:262px;background:linear-gradient(135deg,#f2f7fc,#cde6f6 55%,#d9efc0)" role="img" aria-label="Illustration of a woman on a laptop choosing activities shown as floating icons"></div>
<div class="abs step-num" style="left:834px;top:1653px">2.</div>
<div class="abs step-title right" style="left:560px;top:1760px;width:361px">Choose Your<br>Favorite Activities</div>
<p class="abs step-copy right" style="left:700px;top:1842px;width:221px">Keep the fun of planning and easily budget your entire trip. We'll deal with the hard work and handle all your booking arrangements.</p>
<a class="abs btn green" style="left:808px;top:1915px;width:113px">FIND YOUR FUN!</a>

<!-- proud -->
<div class="abs center h-sec" style="top:2055px">We're proud of what we do</div>
<p class="abs copy" style="left:290px;top:2126px;width:620px;text-align:center">We all know that you get the best travel advice from locals. So why wouldn't you use a local travel agent to help arrange your vacation? We take the time to selectively employ the best agents and concierges from each country to join our team. Our Travel Concierges personally experience every single tour first hand, so they can be in a position to give you the best possible advice and service.</p>
<a class="abs btn blue" style="top:2205px">READ MORE</a>

<!-- step 3 -->
<div class="abs step-num" style="left:278px;top:2273px">3.</div>
<div class="abs step-title" style="left:277px;top:2378px">We Make All The<br>Arrangements</div>
<p class="abs step-copy" style="left:277px;top:2462px;width:240px">Fill out our simple form and we'll use our local expertise to design your ideal vacation package. Best of all, our services are 100% FREE!</p>
<a class="abs btn green" style="left:277px;top:2534px;width:199px">GET A CUSTOM VACATION PROPOSAL</a>
<div class="abs art" style="left:565px;top:2319px;width:361px;height:246px;background:linear-gradient(135deg,#eef6f8,#c6e3f5 55%,#d6edb9)" role="img" aria-label="Illustration of a travel agent greeting a traveller with a suitcase"></div>

<!-- not average -->
<div class="abs center h-sec" style="top:2614px">We're Not Your Average Travel Agency…</div>
<p class="abs copy" style="left:290px;top:2683px;width:620px;text-align:center"><b>TravelAgents</b> can be great as they simplify the process of planning a vacation. But unfortunately their abilities are often limited as usually they've never even been to the country you're looking to go. Once you're out the office and on the plane, there's little they can do to look after you. For example, what happens if when bad weather forces you to reschedule your tours?</p>
<a class="abs btn blue" style="top:2764px">READ MORE</a>

<!-- step 4 -->
<div class="abs art" style="left:295px;top:2860px;width:279px;height:238px;background:linear-gradient(135deg,#f3f8ec,#c9e7f3 55%,#d6eeb4)" role="img" aria-label="Illustration of friends relaxing on a beach with a surfboard and palm trees"></div>
<div class="abs step-num" style="left:834px;top:2814px">4.</div>
<div class="abs step-title right" style="left:560px;top:2922px;width:361px">Relax and Enjoy<br>Your Vacation</div>
<p class="abs step-copy right" style="left:680px;top:3005px;width:241px">Consider us your guardian angels during your stay. We continue to offer support throughout your trip, so you can truly enjoy your vacation, stress free!</p>
<a class="abs btn green" style="left:767px;top:3079px;width:154px">FIND YOUR TRAVEL ANGEL!</a>

<!-- destinations -->
<div class="abs center h-sec" style="top:3165px">Destinations</div>
<div class="abs dest-card" style="left:231px" role="img" aria-label="Aerial view of Grand Cayman coastline"><div class="name">GRAND CAYMAN</div><div class="count">89 ACTIVITIES</div><span class="go">CLICK HERE</span></div>
<div class="abs dest-card" style="left:482px" role="img" aria-label="Aerial view of Little Cayman beach"><div class="name">LITTLE CAYMAN</div><div class="count">6 ACTIVITIES</div><span class="go">CLICK HERE</span></div>
<div class="abs dest-card" style="left:733px" role="img" aria-label="Aerial view of Cayman Brac island"><div class="name">CAYMAN BRAC</div><div class="count">9 ACTIVITIES</div><span class="go">CLICK HERE</span></div>

<!-- favorites -->
<div class="abs center h-sec" style="top:3556px">Our Favorites</div>
<div class="abs rule" style="top:3600px"></div>
<svg class="abs arrow" style="left:175px" viewBox="0 0 22 16"><path d="M21 8H2M8 2L2 8l6 6" fill="none" stroke="#333" stroke-width="1.6"/></svg>
<svg class="abs arrow" style="left:997px" viewBox="0 0 22 16"><path d="M1 8h19M14 2l6 6-6 6" fill="none" stroke="#333" stroke-width="1.6"/></svg>
<div class="abs fav-card" style="left:231px"><div class="ph" style="background:linear-gradient(160deg,#2f6f8f,#3aa0b4 50%,#7fa48a)" role="img" aria-label="Aerial photo of Grand Cayman"></div><div class="lbl">GRAND CAYMAN</div></div>
<div class="abs fav-card" style="left:482px"><div class="ph" style="background:linear-gradient(180deg,#6fc1c9,#4fd0d2 45%,#2fc3c8)" role="img" aria-label="Turquoise shallows of Little Cayman"></div><div class="lbl">LITTLE CAYMAN</div></div>
<div class="abs fav-card" style="left:733px"><div class="ph" style="background:linear-gradient(160deg,#a9c2d2,#5d8fa8 50%,#2f6c88)" role="img" aria-label="Aerial photo of Cayman Brac"></div><div class="lbl">CAYMAN BRAC</div></div>

<!-- footer -->
<div class="abs footer"></div>
<div class="abs island" role="img" aria-label="Illustration of a floating tropical island with a mountain and palm trees"></div>
<div class="abs f-brand"><span class="mark"></span>TideTrip</div>
<div class="abs f-sep" style="left:402px"></div>
<div class="abs f-sep" style="left:582px"></div>
<div class="abs f-sep" style="left:762px"></div>
<div class="abs f-col" style="left:425px"><h4>DESTINATIONS</h4>Grand Cayman<br>Little Cayman<br>Cayman Brac</div>
<div class="abs f-col" style="left:605px"><h4>TERMS OF USE</h4>Privacy Policies<br>Terms of Use<br>Legal Disclaimer</div>
<div class="abs f-col" style="left:785px"><h4>GET IN TOUCH</h4>Support Phone<br><b>+1 555 014 0199</b><br>Email: hello@tidetrip-travel.com</div>
<div class="abs f-copy">COPYRIGHT © 2019 TIDE TRIP. ALL RIGHTS RESERVED.</div>
<div class="abs f-social"><i></i><i></i><i></i><i></i></div>

</body>
</html>
```